Flyer Design

STERLING SHADES
ph:9361 4085
7/41 Pellow Street
Malaga, WA 6069
we need a flyer design for a part broshure part flyer asking for business. well astablished small business for 15years. we manufacture blinds to domestic and commercial. custom made and premium quality. very competitive, free measure and quote even on weekend, plus we offer free fitting to all area. can supply all type of blinds as in big companies. such as roller blinds, roman blinds, timber venetians, slimline venetians, panel glide, vertical blinds, timber shutters etc.

Target Market(s)

new home

Industry/Entity Type

Small Business

Requirements
Nice to have
• a few different type of blinds in partially or part of it may be...

```html
<!DOCTYPE html>
<html lang="en">
<head>
<meta charset="utf-8">
<title>Sterling Shades Flyer</title>
<link href="https://fonts.googleapis.com/css2?family=Open+Sans:wght@700;800&family=Oswald:wght@500&display=swap" rel="stylesheet">
<style>
  :root {
    --bg: #141414;
    --white: #ffffff;
    --brand-blue: #4bb4e6;
    --gold: #e9b221;
    --navy: #1b1a4e;
    --red: #e5202b;
    --ribbon: #d8232a;
    --ink: #0a0a0a;
  }
  * { margin: 0; padding: 0; box-sizing: border-box; }
  html, body { width: 932px; height: 1200px; overflow: hidden; background: var(--bg); }
  .flyer {
    position: relative; width: 932px; height: 1200px; overflow: hidden;
    background: radial-gradient(ellipse at 50% 35%, #2a2a2a 0%, var(--bg) 70%);
    font-family: "Open Sans", Arial, sans-serif; color: var(--white);
  }
  .address {
    position: absolute; top: 16px; left: 0; width: 100%; text-align: center;
    font-size: 45px; font-weight: 700; letter-spacing: -0.5px; white-space: nowrap;
  }
  .brand {
    position: absolute; top: 82px; left: 0; width: 100%; text-align: center;
    font-weight: 800; color: var(--brand-blue); line-height: 0.98;
    font-size: 150px; letter-spacing: -4px;
  }
  .tagline {
    position: absolute; top: 480px; left: 0; width: 100%; text-align: center;
    white-space: nowrap; line-height: 1.1;
  }
  .tagline span {
    display: inline-block; transform: scaleX(0.74); transform-origin: center;
    font-family: "Oswald", "Arial Narrow", sans-serif; font-weight: 500;
    font-size: 82px; color: var(--gold); letter-spacing: -1px;
  }
  .offer-band {
    position: absolute; top: 590px; left: 15px; width: 917px; height: 76px;
    background: var(--navy); text-align: center; white-space: nowrap;
    font-size: 49px; font-weight: 700; line-height: 76px; letter-spacing: -0.5px;
  }
  .weekend {
    position: absolute; top: 660px; left: 0; width: 100%; text-align: center;
    font-size: 46px; font-weight: 700;
  }
  .fitting {
    position: absolute; top: 722px; left: 20px; width: 912px; text-align: center;
    font-size: 48px; font-weight: 700; color: var(--red); letter-spacing: -0.5px; white-space: nowrap;
  }
  .call-ribbon { position: absolute; top: 778px; left: 14px; width: 285px; height: 114px; }
  .call-ribbon svg { position: absolute; inset: 0; }
  .call-label { position: absolute; left: 20px; top: 20px; font-size: 46px; font-weight: 700; line-height: 1; }
  .call-number { position: absolute; left: 68px; top: 70px; font-size: 32px; font-weight: 700; line-height: 1; }
  .photo { position: absolute; border: 2px solid #111; }
  .photo-roller { left: 14px; top: 922px; width: 292px; height: 258px; background: linear-gradient(180deg, #c8542a 0%, #d8653a 55%, #e9e4d8 100%); }
  .photo-vertical { left: 308px; top: 877px; width: 268px; height: 113px; background: linear-gradient(90deg, #d8d5cc, #f1efe9 50%, #dcd9d0); }
  .photo-panel { left: 573px; top: 857px; width: 296px; height: 111px; background: linear-gradient(90deg, #e6e3da, #f7f6f2 60%, #e2dfd6); }
  .photo-dining { left: 706px; top: 931px; width: 226px; height: 269px; background: linear-gradient(180deg, #ecebe6 0%, #f4f3ef 60%, #c99a6b 100%); }
  .photo-timber { left: 135px; top: 990px; width: 308px; height: 210px; background: linear-gradient(180deg, #6b4a2e 0%, #d6a56a 50%, #8a5f38 100%); }
  .photo-venetian { left: 454px; top: 990px; width: 252px; height: 210px; background: linear-gradient(160deg, #8f8a80 0%, #4a4640 55%, #c8b394 100%); }
  .range {
    position: absolute; top: 1024px; left: 0; width: 932px; color: var(--ink);
  }
  .range-title { padding-left: 26px; font-size: 49px; font-weight: 700; letter-spacing: -0.5px; white-space: nowrap; }
  .range-list { text-align: center; font-size: 28px; font-weight: 700; line-height: 1.5; letter-spacing: -0.6px; margin-top: 0; white-space: nowrap; }
</style>
</head>
<body>
<div class="flyer">
  <div class="address">7/41 Pellow Street Malaga, WA 6069</div>

  <div class="brand">STERLING<br>SHADES</div>

  <div class="tagline"><span>Custom Made &amp; Premium Quality</span></div>

  <div class="offer-band">FREE MEASURE AND QUOTE</div>
  <div class="weekend">even on weekend,</div>
  <div class="fitting">PLUS we offer free fitting to all area</div>

  <div class="call-ribbon">
    <svg width="285" height="114" viewBox="0 0 285 114" aria-hidden="true">
      <path d="M0 10 Q0 0 12 0 L0 0 Z" fill="#8e1419"/>
      <path d="M2 14 L258 14 L285 62 L258 112 L14 112 Q2 112 2 100 Z" fill="var(--ribbon)"/>
      <path d="M2 14 L258 14 L272 38 L2 38 Z" fill="#ec4a4f" opacity="0.45"/>
    </svg>
    <div class="call-label">Call</div>
    <div class="call-number">9361 4085</div>
  </div>

  <div class="photo photo-vertical" role="img" aria-label="White vertical blinds with a vase of blue flowers"></div>
  <div class="photo photo-panel" role="img" aria-label="Light patterned panel glide blinds"></div>
  <div class="photo photo-roller" role="img" aria-label="Orange roller blind in a living room"></div>
  <div class="photo photo-dining" role="img" aria-label="Vertical blinds beside a white dining table"></div>
  <div class="photo photo-timber" role="img" aria-label="Timber venetian blinds with sunlight"></div>
  <div class="photo photo-venetian" role="img" aria-label="Dark slimline venetian blinds in a room"></div>

  <div class="range">
    <div class="range-title">Supply all type of blinds:</div>
    <div class="range-list">roller blinds, roman blinds, timber venetians, slimline venetians,<br>panel glide, vertical blinds, timber shutters etc</div>
  </div>
</div>
</body>
</html>
```